New LLC consulting company needs a business card design

I need a business card design for new company in Alexandria Virginia called TK Verdane Consulting LLC. The company is focused on consulting for defense and national security issues with expertise in nuclear and space topics. I would like to see designs that are simple and I am open to colors except for brown.

Target Market(s)

All businesses that are seeking consulting help

Industry/Entity Type

Consulting

Contact Information for Business Card

Name of company - TK Verdane Consulting LLC; name (Delia Hartwig) President; email: hartwigdl47@mailnest.example; Phone: 555-862-4197

Requirements
Must have
• The details described above
Nice to have
• I'm open to all ideas
Should not have
• No brown

```html
<!DOCTYPE html>
<html lang="en">
<head>
<meta charset="utf-8">
<title>TK Verdane Consulting LLC — Business Card</title>
<link rel="stylesheet" href="https://fonts.googleapis.com/css2?family=Roboto:wght@400;500;700&display=swap">
<style>
  :root {
    --brand-blue: #0055a9;
    --card-white: #ffffff;
    --ink-dark: #2b2b2b;
    --rule-grey: #3a3a3a;
    --stage: #1d1d1d;
  }
  * { margin: 0; padding: 0; box-sizing: border-box; }
  html, body {
    width: 1200px;
    height: 1059px;
    overflow: hidden;
    background: var(--stage);
    font-family: "Roboto", Arial, sans-serif;
  }
  .canvas {
    position: relative;
    width: 1200px;
    height: 1059px;
  }
  .card {
    position: absolute;
    left: 247px;
    width: 710px;
    height: 405px;
    border-radius: 26px;
    overflow: hidden;
  }
  .card--front { top: 93px; background: var(--card-white); }
  .card--back  { top: 558px; background: var(--brand-blue); }

  .wordmark {
    position: absolute;
    display: flex;
    align-items: center;
  }
  .wordmark__dot { border-radius: 50%; flex: none; }
  .wordmark__name {
    font-weight: 500;
    line-height: 1;
    text-transform: uppercase;
    white-space: nowrap;
  }
  .wordmark__name span { display: block; }

  .card--front .wordmark { right: 48px; top: 39px; gap: 14px; }
  .card--front .wordmark__dot { width: 120px; height: 120px; background: var(--brand-blue); }
  .card--front .wordmark__name { color: var(--brand-blue); }
  .card--front .wordmark__line1 { font-size: 38px; letter-spacing: 0.5px; }
  .card--front .wordmark__line2 { font-size: 22.5px; margin-top: 6px; letter-spacing: 0.6px; }

  .card--back .wordmark { left: 0; right: 0; top: 0; bottom: 0; justify-content: center; gap: 16px; }
  .card--back .wordmark__dot { width: 148px; height: 148px; background: var(--card-white); }
  .card--back .wordmark__name { color: var(--card-white); }
  .card--back .wordmark__line1 { font-size: 50px; letter-spacing: 0.6px; }
  .card--back .wordmark__line2 { font-size: 29.5px; margin-top: 8px; letter-spacing: 0.8px; }

  .person {
    position: absolute;
    left: 38px;
    top: 250px;
  }
  .person__name {
    font-size: 25px;
    font-weight: 700;
    color: var(--brand-blue);
    letter-spacing: -0.2px;
  }
  .person__title {
    margin-top: 8px;
    font-size: 19px;
    font-weight: 400;
    color: var(--ink-dark);
  }
  .divider {
    position: absolute;
    left: 39px;
    right: 56px;
    top: 325px;
    height: 1.5px;
    background: var(--rule-grey);
  }
  .contact {
    position: absolute;
    left: 37px;
    right: 36px;
    top: 342px;
    display: flex;
    justify-content: space-between;
    align-items: center;
  }
  .contact__item {
    display: flex;
    align-items: center;
    gap: 11px;
    font-size: 19px;
    color: var(--ink-dark);
    letter-spacing: 0.3px;
  }
  .contact__icon { width: 19px; height: 19px; flex: none; }
</style>
</head>
<body>
<main class="canvas">
  <section class="card card--front" aria-label="Business card front">
    <div class="wordmark">
      <div class="wordmark__dot"></div>
      <div class="wordmark__name">
        <span class="wordmark__line1">TK Verdane</span>
        <span class="wordmark__line2">Consulting LLC</span>
      </div>
    </div>

    <div class="person">
      <h1 class="person__name">Delia Hartwig</h1>
      <p class="person__title">President</p>
    </div>

    <div class="divider"></div>

    <div class="contact">
      <div class="contact__item">
        <svg class="contact__icon" viewBox="0 0 24 24" aria-hidden="true">
          <path fill="var(--brand-blue)" d="M6.6 10.8c1.4 2.8 3.8 5.1 6.6 6.6l2.2-2.2c.3-.3.7-.4 1-.2 1.1.4 2.3.6 3.6.6.6 0 1 .4 1 1V20c0 .6-.4 1-1 1C10.6 21 3 13.4 3 4c0-.6.4-1 1-1h3.5c.6 0 1 .4 1 1 0 1.3.2 2.5.6 3.6.1.3 0 .7-.2 1L6.6 10.8z"/>
        </svg>
        <span>555-862-4197</span>
      </div>
      <div class="contact__item">
        <svg class="contact__icon" viewBox="0 0 24 24" aria-hidden="true">
          <path fill="var(--brand-blue)" d="M2 5h20v14H2z"/>
          <path fill="none" stroke="var(--card-white)" stroke-width="2" d="M3 6l9 7 9-7"/>
        </svg>
        <span>hartwigdl47@mailnest.example</span>
      </div>
    </div>
  </section>

  <section class="card card--back" aria-label="Business card back">
    <div class="wordmark">
      <div class="wordmark__dot"></div>
      <div class="wordmark__name">
        <span class="wordmark__line1">TK Verdane</span>
        <span class="wordmark__line2">Consulting LLC</span>
      </div>
    </div>
  </section>
</main>
</body>
</html>
```